Save the date for wedding

A save the date for our wedding. We're looking for a simple and sleek invite. I would prefer not alot of calligraphy. Minimalism is good. The basic info to include is as follows:
Names: Mona and Felix
Date: June 9th
Where: Ottawa, Ontario
In small print please include that there will be a reception in Edmonton AB September 1st for those who cannot make it to Ottawa.
Please see the attached file for a style idea. Doesn’t have to be exactly like that, but something like that.

```html
<!DOCTYPE html>
<html lang="en">
<head>
<meta charset="utf-8">
<title>Save the Date — Mona &amp; Felix</title>
<link rel="stylesheet" href="https://fonts.googleapis.com/css2?family=Josefin+Sans:wght@700&family=Playfair+Display:wght@700&family=Lato:wght@400&display=swap">
<style>
  :root {
    --slate: #666867;
    --paper: #ffffff;
  }
  html, body {
    margin: 0;
    padding: 0;
    overflow: hidden;
    background: var(--slate);
  }
  .save-the-date {
    position: relative;
    width: 1200px;
    height: 851px;
    background: var(--slate);
    color: var(--paper);
    overflow: hidden;
  }
  .frame {
    position: absolute;
    inset: 0;
  }
  .line {
    position: absolute;
    left: 0;
    width: 100%;
    margin: 0;
    text-align: center;
    line-height: 1;
    white-space: nowrap;
  }
  .date {
    top: 80px;
    font-family: "Josefin Sans", sans-serif;
    font-weight: 700;
    font-size: 56px;
  }
  .names {
    font-family: "Playfair Display", serif;
    font-weight: 700;
    font-size: 182px;
    letter-spacing: -1px;
  }
  .names--first { top: 152px; }
  .names--second { top: 318px; }
  .ring-icon {
    position: absolute;
    left: 549px;
    top: 514px;
    width: 62px;
    height: 62px;
  }
  .venue {
    top: 612px;
    font-family: "Josefin Sans", sans-serif;
    font-weight: 700;
    font-size: 46px;
  }
  .note {
    top: 747px;
    font-family: "Lato", sans-serif;
    font-weight: 400;
    font-size: 22px;
  }
</style>
</head>
<body>
<main class="save-the-date">
  <svg class="frame" width="1200" height="851" viewBox="0 0 1200 851" aria-hidden="true">
    <rect x="22" y="22" width="1156" height="807" rx="62" ry="62"
          fill="none" stroke="var(--paper)" stroke-width="17"/>
  </svg>

  <p class="line date">June 9, 2018</p>
  <h1 class="line names names--first">Mona</h1>
  <h1 class="line names names--second">&amp; Felix</h1>

  <svg class="ring-icon" viewBox="0 0 62 62" aria-hidden="true">
    <circle cx="31" cy="31" r="31" fill="var(--paper)"/>
    <path d="M25 14 h12 l4 6 -10 6 -10 -6 z" fill="var(--slate)"/>
    <circle cx="31" cy="37" r="12" fill="none" stroke="var(--slate)" stroke-width="5"/>
  </svg>

  <p class="line venue">Ottawa, Ontario</p>
  <p class="line note">Reception in Edmonton AB September 1st for those who cannot make it to Ottawa.</p>
</main>
</body>
</html>
```